Buch-/E-Book-Cover-Design für Fortsetzung  des 1. Bands
Buch-/E-Book-Cover-Design für Fortsetzung des 1. Bands
Zielgruppe
Ich suche ein Cover für mein Buch (Print und eBook)
Titel: 'Kaskade 7.2 - Umbruch'
Aufgabenstellung
Das Buch ist die Fortsetzung von Band 1: Kaskade 7.2 - Verzweigung. Ich suche ein Cover, das von der Gestaltung her zu Band 1 passt.
Stichpunkte zur Orientierung:
Augmented Reality, Cyberwelten, Deep Learning, Designerkinder, Evolution, tieflernende Algorithmen, Künstliche Intelligenz, Virtuelle Realität, Nanobots, Action, Abenteuer, Liebe, Leidenschaft, Humor, Computer, DNA, Technologie, Magie, Zeppelin, Wirbelsturm

```html
<!DOCTYPE html>
<html lang="de">
<head>
<meta charset="utf-8">
<title>Kaskade 7.2 – Umbruch</title>
<link rel="stylesheet" href="https://fonts.googleapis.com/css2?family=Staatliches&display=swap">
<style>
  :root {
    --bg: #000000;
    --ink: #f2fdfe;
    --glow: #2fd9ea;
    --glow-deep: #0b6f86;
  }
  html, body {
    margin: 0;
    padding: 0;
    width: 864px;
    height: 1200px;
    overflow: hidden;
    background: var(--bg);
  }
  .cover {
    position: relative;
    width: 864px;
    height: 1200px;
    background: var(--bg);
    overflow: hidden;
    font-family: "Staatliches", "Arial Narrow", sans-serif;
    color: var(--ink);
    text-align: center;
  }
  .filters {
    position: absolute;
    width: 0;
    height: 0;
  }
  .cover__author,
  .cover__title,
  .cover__subtitle {
    position: absolute;
    left: 0;
    right: 0;
    margin: 0;
    font-weight: 400;
    line-height: 1;
    text-transform: uppercase;
    filter: url(#worn-type) drop-shadow(0 0 5px rgba(47, 217, 234, 0.6));
  }
  .cover__author {
    top: 66px;
    font-size: 56px;
    letter-spacing: 3px;
  }
  .cover__title {
    top: 150px;
    font-size: 134px;
    letter-spacing: 5px;
  }
  .cover__subtitle {
    top: 300px;
    font-size: 56px;
    letter-spacing: 8px;
  }
  .cover__subtitle .dash {
    letter-spacing: 0;
    color: var(--glow);
  }
  .cover__artwork {
    position: absolute;
    left: 0;
    top: 400px;
    width: 864px;
    height: 800px;
  }
</style>
</head>
<body>
  <main class="cover">
    <svg class="filters" aria-hidden="true" focusable="false">
      <filter id="worn-type" x="-5%" y="-20%" width="110%" height="140%">
        <feTurbulence type="fractalNoise" baseFrequency="0.9" numOctaves="2" seed="7" result="grain"/>
        <feColorMatrix in="grain" type="matrix"
          values="0 0 0 0 0  0 0 0 0 0  0 0 0 0 0  0 0 0 -2.6 1.55" result="holes"/>
        <feComposite in="SourceGraphic" in2="holes" operator="in" result="worn"/>
        <feDisplacementMap in="worn" in2="grain" scale="3" xChannelSelector="R" yChannelSelector="G"/>
      </filter>
    </svg>

    <p class="cover__author">Pel Amarsdottir</p>
    <h1 class="cover__title">Kaskade 7.2</h1>
    <p class="cover__subtitle"><span class="dash">-</span>Umbruch<span class="dash">-</span></p>

    <svg class="cover__artwork" viewBox="0 0 864 800" role="img"
         aria-label="Leuchtend türkiser Fingerabdruck inmitten eines Regens aus Binärziffern, durchzogen von einem diagonalen Lichtstreif auf schwarzem Grund">
      <defs>
        <linearGradient id="artwork-fade" x1="0" y1="0" x2="0" y2="1">
          <stop offset="0" stop-color="#000000"/>
          <stop offset="0.12" stop-color="#03151c"/>
          <stop offset="0.45" stop-color="#0a3a48"/>
          <stop offset="0.75" stop-color="#062630"/>
          <stop offset="1" stop-color="#000000"/>
        </linearGradient>
        <radialGradient id="artwork-band" cx="0.5" cy="0.5" r="0.5">
          <stop offset="0" stop-color="#13748a" stop-opacity="0.85"/>
          <stop offset="0.6" stop-color="#0b4b5c" stop-opacity="0.5"/>
          <stop offset="1" stop-color="#000000" stop-opacity="0"/>
        </radialGradient>
        <radialGradient id="artwork-core" cx="0.45" cy="0.45" r="0.55">
          <stop offset="0" stop-color="#46f2ff"/>
          <stop offset="0.55" stop-color="#22c8dc" stop-opacity="0.9"/>
          <stop offset="0.85" stop-color="#0f8ea3" stop-opacity="0.45"/>
          <stop offset="1" stop-color="#0b6f86" stop-opacity="0"/>
        </radialGradient>
        <linearGradient id="artwork-streak" x1="0" y1="1" x2="1" y2="0">
          <stop offset="0" stop-color="#2fd9ea" stop-opacity="0"/>
          <stop offset="0.45" stop-color="#bffcff" stop-opacity="0.95"/>
          <stop offset="1" stop-color="#2fd9ea" stop-opacity="0"/>
        </linearGradient>
      </defs>
      <rect x="0" y="0" width="864" height="800" fill="url(#artwork-fade)"/>
      <ellipse cx="432" cy="360" rx="470" ry="260" fill="url(#artwork-band)"/>
      <ellipse cx="425" cy="390" rx="175" ry="235" transform="rotate(-12 425 390)" fill="url(#artwork-core)"/>
      <polygon points="110,605 800,400 806,412 118,614" fill="url(#artwork-streak)"/>
    </svg>
  </main>
</body>
</html>
```